Stationary package for modern new church start
Stationary for Bright Harbor Ministries
Stationary package for modern new church start  - Religion and Spirituality
Creative Brief
Professional
Daniel Mercer
Pastor
Bright Harbor Ministries P.O. Box 67890 Atlanta, GA 30318 The following P.O. Box is a generate one until I obtain one tomorrow. I will provide you with the correct P.O. Box sometime tomorrow or on Friday.
pastormercer@bhmx.org
www.bhmx.org
Please provide me with a complete stationary package that includes: Business Cards Letterhead Pen and pencil Email Signature USB Envelope Folder Fax Option Thank you Card front & Back Compliment Slip CD and CD Cover
Please include the following on the back: The Logo our our Ministry and our email address

```html
<!DOCTYPE html>
<html lang="en">
<head>
<meta charset="utf-8">
<title>Bright Harbor Ministries – Business Card</title>
<link rel="stylesheet" href="https://fonts.googleapis.com/css2?family=Montserrat:wght@400;600;800&display=swap">
<style>
  :root {
    --page: #e9e9eb;
    --card: #ffffff;
    --red: #d0141b;
    --red-dark: #a60d12;
    --blue: #22a7e0;
    --ink: #3a3a3a;
    --muted: #777777;
  }
  * { margin: 0; padding: 0; box-sizing: border-box; }
  html, body { width: 1200px; height: 901px; overflow: hidden; }
  body {
    background: var(--page);
    font-family: "Montserrat", sans-serif;
    display: flex;
    align-items: center;
    justify-content: center;
    gap: 40px;
  }
  .card {
    position: relative;
    width: 540px;
    height: 309px;
    background: var(--card);
    border-radius: 18px;
    overflow: hidden;
    box-shadow: 0 6px 18px rgba(0,0,0,.15);
  }
  .card__band { position: absolute; inset: 0; width: 100%; height: 100%; }
  .card__web {
    position: absolute;
    color: #fff;
    font-size: 12px;
    font-weight: 600;
    letter-spacing: .5px;
  }
  .brand {
    display: flex;
    align-items: center;
    gap: 10px;
  }
  .brand__dot {
    width: 26px; height: 26px; border-radius: 50%;
    background: var(--red);
    flex: none;
  }
  .brand__name {
    color: var(--red);
    font-weight: 800;
    line-height: 1.05;
  }
  /* back */
  .card--back .brand { position: absolute; left: 170px; top: 108px; }
  .card--back .brand__name { font-size: 26px; width: 250px; }
  .card--back .card__web { left: 34px; bottom: 24px; transform: rotate(-14deg); transform-origin: left bottom; }
  /* front */
  .card--front .brand { position: absolute; left: 150px; top: 34px; }
  .card--front .brand__dot { width: 20px; height: 20px; }
  .card--front .brand__name { font-size: 20px; }
  .card--front .card__web { left: 30px; top: 260px; transform: rotate(-90deg); transform-origin: left top; }
  .contact {
    position: absolute;
    left: 150px; top: 110px;
    display: grid;
    grid-template-columns: 170px 1fr;
    column-gap: 24px;
    color: var(--ink);
    font-size: 11px;
    line-height: 1.7;
  }
  .contact__name { font-size: 16px; font-weight: 800; color: var(--red); line-height: 1.3; }
  .contact__title { color: var(--muted); font-weight: 600; margin-bottom: 8px; }
  .contact__rule { border-left: 2px solid var(--blue); padding-left: 14px; }
</style>
</head>
<body>
  <article class="card card--back" aria-label="Card back">
    <svg class="card__band" viewBox="0 0 540 309" aria-hidden="true">
      <path d="M0 150 C120 230 300 250 540 230 L540 309 L0 309 Z" fill="var(--red)"/>
      <path d="M0 150 C120 230 300 250 540 230" fill="none" stroke="var(--blue)" stroke-width="4"/>
      <path d="M0 250 C150 300 360 300 540 290 L540 309 L0 309 Z" fill="var(--red-dark)" opacity=".5"/>
    </svg>
    <div class="brand">
      <span class="brand__dot"></span>
      <span class="brand__name">Bright Harbor Ministries</span>
    </div>
    <span class="card__web">www.bhmx.org</span>
  </article>

  <article class="card card--front" aria-label="Card front">
    <svg class="card__band" viewBox="0 0 540 309" aria-hidden="true">
      <path d="M0 0 L80 0 C110 100 110 210 80 309 L0 309 Z" fill="var(--red)"/>
      <path d="M80 0 C110 100 110 210 80 309" fill="none" stroke="var(--blue)" stroke-width="4"/>
    </svg>
    <div class="brand">
      <span class="brand__dot"></span>
      <span class="brand__name">Bright Harbor Ministries</span>
    </div>
    <div class="contact">
      <div>
        <p class="contact__name">Daniel Mercer</p>
        <p class="contact__title">Pastor</p>
        <p>P.O. Box 67890</p>
        <p>Atlanta, GA 30318</p>
      </div>
      <div class="contact__rule">
        <p>Cell: 404 555 0132</p>
        <p>Office: 404 555 0198</p>
        <p>Fax: 404 555 0177</p>
        <p>pastormercer@bhmx.org</p>
        <p>www.bhmx.org</p>
      </div>
    </div>
    <span class="card__web">www.bhmx.org</span>
  </article>
</body>
</html>
```